Lantern Method of Ascent Programme Graphic

Please refer to attached graphic.
I wish to redesign this graphic to represent a programme of work that we (Vendro) deliver to our customers.
The design represents 9 steps ( 3 steps at each of 3 levels) and is all about implementing the 'Lantern Method of Ascent'

I like the fact that the increasing business growth is evident when you are progressing through the stages, but the current graphic looks dated and the colours are not working.
I would also like to incorporate the LMA logo we have created.

Target Market(s)

IT Sector - businesses looking to grow

Industry/Entity Type

We are a digital marketing company

Requirements
Must have
• Clear, concise design
Should not have
• Design must not be complicated

```html
<!DOCTYPE html>
<html lang="en">
<head>
<meta charset="utf-8">
<title>Lantern Method of Ascent – Programme</title>
<link rel="stylesheet" href="https://fonts.googleapis.com/css2?family=Outfit:wght@300;400;500;600;700&family=Montserrat:wght@700&display=swap">
<style>
  :root {
    --bg: #02164f;
    --teal: #00bfa6;
    --teal-line: #14d4d0;
    --blue: #0066ff;
    --violet: #4514ff;
    --violet-line: #4a22f0;
    --brand: #1e9ddc;
    --white: #ffffff;
    --chip: #02164f;
  }
  * { margin: 0; padding: 0; box-sizing: border-box; }
  html, body { width: 1200px; height: 675px; overflow: hidden; background: var(--bg); }
  .programme { display: block; width: 1200px; height: 675px; font-family: "Outfit", sans-serif; }
  .axis-label { font-family: "Montserrat", sans-serif; font-weight: 700; font-size: 40px; letter-spacing: 14px; fill: var(--white); }
  .stage-title { font-weight: 600; font-size: 46px; letter-spacing: 2px; fill: var(--white); }
  .step { font-weight: 500; font-size: 31px; fill: var(--white); }
  .step-icon { fill: var(--chip); }
  .glyph { fill: none; stroke: var(--white); stroke-width: 2.5; stroke-linecap: round; }
  .caption { font-weight: 500; font-size: 38px; fill: var(--white); }
  .subcaption { font-weight: 300; font-size: 38px; }
  .brand-name { font-weight: 700; fill: var(--brand); }
</style>
</head>
<body>
<svg class="programme" viewBox="0 0 2576 1449" xmlns="http://www.w3.org/2000/svg" role="img" aria-label="Lantern Method of Ascent programme: three stages of three steps rising in business value">
  <rect width="2576" height="1449" fill="var(--bg)"/>

  <!-- Brand column -->
  <g class="brand">
    <rect x="300" y="540" width="34" height="34" fill="var(--brand)"/>
    <text class="brand-name" x="350" y="572" font-size="58">LMA</text>
    <line x1="197" y1="794" x2="517" y2="794" stroke="var(--brand)" stroke-width="4"/>
    <text class="brand-name" x="357" y="975" font-size="86" text-anchor="middle">Vendro</text>
  </g>

  <!-- Value axis -->
  <g class="value-axis" stroke="var(--white)" stroke-width="6" fill="none" stroke-linecap="round">
    <line x1="726" y1="965" x2="726" y2="1190"/>
    <line x1="726" y1="262" x2="726" y2="420"/>
    <polyline points="703,283 726,260 749,283"/>
  </g>
  <text class="axis-label" transform="translate(741 692) rotate(-90)" text-anchor="middle">BUSINESS VALUE</text>

  <!-- Stage 1 -->
  <g class="stage stage-lantern">
    <polyline points="806,1007 806,908 1462,633 1462,728" fill="none" stroke="var(--teal-line)" stroke-width="5"/>
    <polygon points="806,1042 1462,768 1462,1042" fill="var(--teal)"/>
    <text class="stage-title" transform="translate(1118 845) rotate(-22.7)" text-anchor="middle">LANTERN</text>
    <g stroke="var(--chip)" stroke-width="2"><line x1="1237" y1="908" x2="1390" y2="908"/><line x1="1237" y1="966" x2="1390" y2="966"/></g>
    <text class="step" x="1393" y="892" text-anchor="end">PERSONAS</text>
    <text class="step" x="1393" y="949" text-anchor="end">DATABASE</text>
    <text class="step" x="1393" y="1005" text-anchor="end">SYSTEMS</text>
    <circle class="step-icon" cx="1423" cy="881" r="22"/>
    <g class="glyph"><circle cx="1415" cy="876" r="4"/><circle cx="1431" cy="876" r="4"/><path d="M1407 891 q8 -9 16 0 q8 -9 16 0"/></g>
    <circle class="step-icon" cx="1423" cy="938" r="22"/>
    <g class="glyph"><rect x="1411" y="927" width="24" height="7"/><rect x="1411" y="937" width="24" height="7"/><rect x="1411" y="947" width="24" height="2"/></g>
    <circle class="step-icon" cx="1423" cy="994" r="22"/>
    <g class="glyph"><rect x="1411" y="984" width="24" height="16"/><line x1="1423" y1="1000" x2="1423" y2="1006"/></g>
    <polyline points="806,1092 806,1189 1462,1189 1462,1095" fill="none" stroke="var(--teal-line)" stroke-width="5"/>
    <text class="caption" x="1133" y="1105" text-anchor="middle">Numbers that Matter</text>
    <text class="subcaption" x="1133" y="1149" text-anchor="middle" fill="var(--teal)">Foundation Metrics</text>
  </g>

  <!-- Stage 2 -->
  <g class="stage stage-method">
    <polyline points="1527,710 1527,612 1941,438 1941,535" fill="none" stroke="var(--blue)" stroke-width="5"/>
    <polygon points="1527,745 1941,575 1941,1042 1527,1042" fill="var(--blue)"/>
    <text class="stage-title" transform="translate(1735 600) rotate(-22.7)" text-anchor="middle">METHOD</text>
    <g stroke="var(--chip)" stroke-width="2"><line x1="1636" y1="908" x2="1850" y2="908"/><line x1="1636" y1="966" x2="1850" y2="966"/></g>
    <text class="step" x="1852" y="892" text-anchor="end">MESSAGING</text>
    <text class="step" x="1852" y="949" text-anchor="end">LEADS</text>
    <text class="step" x="1852" y="1005" text-anchor="end">PIPELINE</text>
    <circle class="step-icon" cx="1893" cy="881" r="22"/>
    <g class="glyph"><rect x="1881" y="871" width="24" height="16"/><line x1="1886" y1="877" x2="1900" y2="877"/><line x1="1886" y1="882" x2="1896" y2="882"/></g>
    <circle class="step-icon" cx="1893" cy="938" r="22"/>
    <g class="glyph"><circle cx="1888" cy="932" r="5"/><circle cx="1899" cy="934" r="4"/><path d="M1879 950 q9 -12 18 0"/></g>
    <circle class="step-icon" cx="1893" cy="994" r="22"/>
    <g class="glyph"><path d="M1881 986 h16 a6 6 0 0 1 0 12 h-12 a5 5 0 0 0 0 10"/></g>
    <polyline points="1527,1092 1527,1189 1941,1189 1941,1095" fill="none" stroke="var(--blue)" stroke-width="5"/>
    <text class="caption" x="1734" y="1105" text-anchor="middle">Weekly Scorecard</text>
    <text class="subcaption" x="1734" y="1149" text-anchor="middle" fill="var(--blue)">Tactical Execution</text>
  </g>

  <!-- Stage 3 -->
  <g class="stage stage-ascent">
    <polyline points="2003,520 2003,422 2417,248 2417,345" fill="none" stroke="var(--violet-line)" stroke-width="5"/>
    <polygon points="2003,555 2417,383 2417,1042 2003,1042" fill="var(--violet)"/>
    <text class="stage-title" transform="translate(2208 408) rotate(-22.7)" text-anchor="middle">ASCENT</text>
    <g stroke="var(--chip)" stroke-width="2"><line x1="2160" y1="908" x2="2330" y2="908"/><line x1="2160" y1="966" x2="2330" y2="966"/></g>
    <text class="step" x="2332" y="892" text-anchor="end">SALES</text>
    <text class="step" x="2332" y="949" text-anchor="end">NURTURE</text>
    <text class="step" x="2332" y="1005" text-anchor="end">REFERENCE</text>
    <circle class="step-icon" cx="2366" cy="881" r="22"/>
    <g class="glyph"><line x1="2357" y1="891" x2="2357" y2="883"/><line x1="2364" y1="891" x2="2364" y2="877"/><line x1="2371" y1="891" x2="2371" y2="871"/></g>
    <circle class="step-icon" cx="2366" cy="938" r="22"/>
    <g class="glyph"><path d="M2354 942 q12 14 24 0"/><line x1="2366" y1="942" x2="2366" y2="928"/><path d="M2366 932 q-6 -6 -8 0"/></g>
    <circle class="step-icon" cx="2366" cy="994" r="22"/>
    <g class="glyph"><rect x="2355" y="983" width="16" height="20"/><circle cx="2372" cy="999" r="5"/><line x1="2376" y1="1003" x2="2380" y2="1007"/></g>
    <polyline points="2003,1092 2003,1189 2417,1189 2417,1095" fill="none" stroke="var(--violet-line)" stroke-width="5"/>
    <text class="caption" x="2210" y="1105" text-anchor="middle">Monthly Scorecard</text>
    <text class="subcaption" x="2210" y="1149" text-anchor="middle" fill="var(--violet)">Strategic Review</text>
  </g>
</svg>
</body>
</html>
```